Landing Page for Bathroom Remodeling Webpage - Desktop and Mobile

I am looking for some help designing the "above the fold" area for my bathroom remodeling service page. Looking for something a little different than the rest. Typically remodeling companies just put a nice picture of a bathroom remodel but I would like to do something a little different / more creative. Below is a link to the current wireframe we are working on.
Current website is located at brellforgeplains.com
Again the biggest thing I am looking for is a design for the very top section but would love help on the rest of the page as well. You will see by viewing the link below the type of information we are looking to include on the page:
PLEASE DO INCLUDE WHAT THE MOBILE VERSION WOULD LOOK LIKE AS WELL.
Wireframe:
https://xd.quillvarn.com/view/3f8a1b2c-90de-4e7f-8a6b-1c2d3e4f5a6b-841c/
There are also comments in the link above you can read as well.
We like the idea of something interactive such as this...
https://pixelmoor.com/shots/5149273-Valdor-Scooter-Store-Animation
Attached is also the logo we want to use going forward
Target Market(s)
Residential homeowners, 30 years old+ with professional careers
Number of Pages Required
1 page
Look and feel

```html
<!DOCTYPE html>
<html lang="en">
<head>
<meta charset="utf-8">
<title>Brellforge – Bathroom Remodeling Landing Page</title>
<link href="https://fonts.googleapis.com/css2?family=Open+Sans:wght@300;400;600;700&family=Poppins:wght@500;600;700&family=Merriweather:wght@700;900&display=swap" rel="stylesheet">
<style>
:root{
  --stage:#e8e8eb;
  --navy:#1f2a4d;
  --red:#f2403f;
  --green:#1db43a;
  --blue:#3b8fe0;
  --hero-top:#3b5374;
  --hero-bottom:#23364f;
  --mist:#dedfe6;
  --slate:#c6c9d5;
  --card:#eef1f6;
  --ink:#2b2f3a;
  --muted:#7a7f8c;
  --white:#ffffff;
  --footer:#e1e2e6;
  --tick:#2aa84a;
}
*{box-sizing:border-box;margin:0;padding:0}
html,body{width:782px;height:1200px;overflow:hidden}
body{background:var(--stage);font-family:"Open Sans",sans-serif;color:var(--ink);position:relative}
.page{position:absolute;background:var(--white);overflow:hidden;box-shadow:0 1px 4px rgba(0,0,0,.12)}
.page--desktop{left:40px;top:26px;width:288px;height:1144px}
.page--compact{left:371px;top:68px;width:368px;height:855px}
.section{position:relative;width:100%}
.center{text-align:center}

/* header */
.site-header{display:flex;align-items:center;background:var(--white)}
.brand{display:flex;align-items:center;gap:2px;color:var(--red);font-family:"Poppins",sans-serif;font-weight:700;letter-spacing:.2px}
.brand-dot{border-radius:50%;background:var(--red);flex:none}
.main-nav{display:flex;font-weight:600;color:var(--ink)}
.estimate{margin-left:auto;background:var(--green);color:var(--white);font-weight:700;text-align:center;height:100%;display:flex;flex-direction:column;justify-content:center;line-height:1.25}

/* hero */
.hero{background:linear-gradient(160deg,var(--hero-top),var(--hero-bottom));color:var(--white)}
.hero-photo{position:absolute;inset:0;background:radial-gradient(ellipse at 62% 45%,rgba(150,170,195,.45),rgba(35,54,79,0) 60%)}
.hero-title{position:absolute;font-weight:300;line-height:1.1}
.hero-accent{display:inline-block;font-family:"Merriweather",serif;font-weight:900;border:1px solid var(--blue);transform:skewX(-4deg)}
.hero-sub{position:absolute;line-height:1.35}
.hero-sub b{font-weight:700}
.btn-services{position:absolute;background:var(--blue);color:var(--white);font-weight:700;border-radius:2px;display:flex;align-items:center;justify-content:center}

/* bars */
.cta-bar{background:var(--navy);color:var(--white);display:flex;align-items:center;justify-content:center;font-weight:700}
.btn-red{background:var(--red);color:var(--white);font-weight:700;border-radius:3px;display:flex;align-items:center;justify-content:center}

/* projects */
.projects{background:var(--mist)}
.section-title{font-weight:400;color:var(--ink);text-align:center}
.project{position:absolute;background:linear-gradient(135deg,#eef0f2,#c9c3bb 55%,#8a7868)}
.project--two{background:linear-gradient(135deg,#f1f1ef,#b88d6c 55%,#5d6470)}
.project-caption{position:absolute;left:0;right:0;bottom:0;background:rgba(40,40,45,.6);color:var(--white);line-height:1.5}
.more{position:absolute;left:50%;transform:translateX(-50%);text-align:center;color:var(--ink)}
.more-circle{margin:0 auto;border-radius:50%;background:var(--white);border:1px solid #b7bac4;display:flex;align-items:center;justify-content:center;color:#8a8e99;font-weight:300}

.bath{background:var(--slate)}
.bath-text{position:absolute;left:50%;transform:translateX(-50%);text-align:center;line-height:1.35}

/* materials */
.icon-list{display:block;margin:0 auto}
.material-card{position:absolute;background:var(--white);border:1px solid #e1e4ea;font-family:"Poppins",sans-serif;font-weight:600}
.material-list{position:absolute;background:var(--card);color:var(--muted);line-height:1.9}
.material-list span::before{content:"✔";color:var(--navy);margin-right:3px}
.price-icon{border-radius:50%;border:1px solid #555;display:flex;align-items:center;justify-content:center;margin:0 auto;background:#d9d9d9;font-weight:700}
.price-card{position:absolute;background:#dde4ee;text-align:center}
.price-card--best{background:var(--white);box-shadow:0 1px 5px rgba(0,0,0,.15)}
.price-name{font-family:"Poppins",sans-serif;font-weight:600;color:#4a4f5c}
.price-card--best .price-name{color:var(--blue)}
.price-amount{font-family:"Poppins",sans-serif;font-weight:700;color:#4a4f5c}
.price-list{text-align:left;color:var(--muted);line-height:1.85}
.price-list span::before{content:"✔";color:var(--tick);margin-right:3px}
.badge{position:absolute;background:var(--blue);color:var(--white);font-weight:700}

/* scheduler */
.scheduler{background:#f3f4f7}
.clock-photo{position:absolute;left:0;top:0;bottom:0;width:128px;background:radial-gradient(circle at 10% 60%,#f6f6f6 30%,#b9bcc2 48%,#eceef1 60%)}
.booking{position:absolute;background:var(--white);border:1px solid #e4e6eb;color:var(--muted);line-height:1.4}
.booking b{color:var(--ink)}
.steps{position:absolute;color:var(--muted);line-height:1.4}
.steps h4{font-family:"Poppins",sans-serif;color:var(--ink);font-weight:600}

/* articles */
.article{position:absolute;background:var(--white);border:1px solid #e3e5ea}
.article-img{height:26px}
.article-meta{padding:2px 6px;color:var(--muted);line-height:1.5}
.btn-blog{position:absolute;background:#7b8290;color:var(--white);font-weight:700;display:flex;align-items:center;justify-content:center}
.faq-row{display:flex;justify-content:space-between;border-bottom:1px solid #e3e5ea;font-weight:700;color:var(--ink)}

.contact{background:var(--navy);color:var(--white);text-align:center}
.contact h3{font-family:"Poppins",sans-serif;font-weight:600}
.footer{background:var(--footer)}
.social{display:flex}
.social i{border-radius:50%;background:#9aa0ab;display:block}
.foot-col{position:absolute;color:var(--ink);line-height:1.45}
.foot-col h5{font-weight:700;margin-bottom:2px}
.copyright{position:absolute;left:0;right:0;border-top:1px solid #c9ccd3;display:flex;justify-content:space-between;color:var(--ink)}
.copyright b{font-weight:700}
</style>
</head>
<body>

<!-- Desktop layout -->
<main class="page page--desktop">
  <header class="section site-header" style="height:19px;padding-left:7px">
    <div class="brand" style="font-size:6.5px"><span class="brand-dot" style="width:6px;height:6px"></span>BRELLFORGE</div>
    <nav class="main-nav" style="font-size:3.6px;gap:11px;margin-left:29px"><span>Home</span><span>Services</span><span>Gallery</span><span>Blog</span><span>About</span><span>Contact</span></nav>
    <div class="estimate" style="width:56px;font-size:4.2px">GET AN ESTIMATE<br>515-555-0142</div>
  </header>

  <section class="section hero" style="height:154px">
    <div class="hero-photo" role="img" aria-label="Chrome bath faucet against dark blue panelled wall"></div>
    <h1 class="hero-title" style="left:18px;top:46px;font-size:10.5px">Making homes<br><span class="hero-accent" style="font-size:11px;padding:0 3px;margin-left:-4px;margin-top:1px">that matter.</span></h1>
    <p class="hero-sub" style="left:18px;top:79px;font-size:4.2px">We provide <b>home remodeling services</b> to<br>help you build a home you love.</p>
    <div class="btn-services" style="left:19px;top:97px;width:32px;height:11px;font-size:2.6px">OUR SERVICES</div>
  </section>

  <div class="section cta-bar" style="height:19px;font-size:3.8px;gap:18px;padding-left:10px">
    <span>Schedule a free in home consultation via our online appointment scheduling system</span>
    <span class="btn-red" style="width:33px;height:13px;font-size:4px">Schedule</span>
  </div>

  <section class="section projects" style="height:151px">
    <h2 class="section-title" style="padding-top:11px;font-size:6.5px">Get inspired by similar projects</h2>
    <div class="project" style="left:19px;top:31px;width:120px;height:79px" role="img" aria-label="White kitchen with island and pendant lights">
      <div class="project-caption" style="font-size:3.6px;padding:2px 3px">Kitchen and Complete Home Remodel<br>@ in Woodland Hills, CA</div></div>
    <div class="project project--two" style="left:150px;top:31px;width:119px;height:79px" role="img" aria-label="Kitchen with wood backsplash and small dining table">
      <div class="project-caption" style="font-size:3.6px;padding:2px 3px">Complete Kitchen Remodel<br>@ in West Hollywood, CA</div></div>
    <div class="more" style="top:118px;font-size:2.6px"><div class="more-circle" style="width:14px;height:14px;font-size:7px">+</div><div style="margin-top:2px">Show me more</div></div>
  </section>

  <section class="section bath" style="height:93px">
    <h2 class="section-title" style="padding-top:12px;font-size:6.5px">Bathroom Remodeling Made Simple.</h2>
    <p class="bath-text" style="top:28px;width:132px;font-size:2.9px">Bathroom remodel can be complex, but when completed in an eco-friendly and sustainable manner can also drastically monthly bills and give you the satisfaction of reducing your carbon footprint in the process. A bathroom remodels range anywhere from updating your plumbing fixture, to making more efficient use of the space, to building the in-home spa of your dreams. A bathroom remodel is subjective, but homeowners are generally faced with the same universal challenges regardless of project scape.</p>
    <div class="more" style="top:63px;font-size:2.6px"><div class="more-circle" style="width:14px;height:14px;font-size:7px">+</div><div style="margin-top:2px">Show me more</div></div>
  </section>

  <section class="section" style="height:126px">
    <svg class="icon-list" width="11" height="9" viewBox="0 0 11 9" style="margin-top:5px"><g fill="#3d4a66"><rect width="2" height="1.6"/><rect x="3" width="8" height="1.6"/><rect y="2.5" width="2" height="1.6"/><rect x="3" y="2.5" width="8" height="1.6"/><rect y="5" width="2" height="1.6"/><rect x="3" y="5" width="8" height="1.6"/><rect y="7.4" width="2" height="1.6"/><rect x="3" y="7.4" width="8" height="1.6"/></g></svg>
    <h2 class="section-title" style="margin-top:4px;font-size:5.6px;letter-spacing:.2px">Material Selections</h2>
    <p class="center" style="margin:5px auto 0;width:200px;font-size:3.3px;color:var(--muted);line-height:1.6">For your kitchen remodel there will be material selections you will have to make. Use the lists below to see some of the materials we use in our Clive, IA kitchen remodeling work:</p>
    <div class="material-card" style="left:40px;top:50px;width:47px;height:41px;font-size:3.6px;padding:28px 0 0 7px">Electrical</div>
    <div class="material-card" style="left:93px;top:50px;width:47px;height:41px;font-size:3.6px;padding:28px 0 0 7px">Plumbing</div>
    <div class="material-card" style="left:145px;top:50px;width:47px;height:41px;font-size:3.6px;padding:28px 0 0 7px">Tile &amp; Flooring</div>
    <div class="material-card" style="left:198px;top:50px;width:47px;height:41px;font-size:3.6px;padding:28px 0 0 7px">Finishes</div>
    <svg style="position:absolute;left:47px;top:57px" width="6" height="9" viewBox="0 0 6 9"><path d="M3 0L0 5h2.5L1.5 9 6 3.5H3.5L5 0z" fill="#3d4a66"/></svg>
    <svg style="position:absolute;left:100px;top:57px" width="6" height="8" viewBox="0 0 6 8"><path d="M3 0C2 2.5 0 4 0 5.5a3 2.5 0 006 0C6 4 4 2.5 3 0z" fill="#3d4a66"/></svg>
    <svg style="position:absolute;left:152px;top:57px" width="10" height="8" viewBox="0 0 10 8"><g fill="#3d4a66"><rect width="4.5" height="3.5"/><rect x="5.5" width="4.5" height="3.5"/><rect y="4.5" width="4.5" height="3.5"/><rect x="5.5" y="4.5" width="4.5" height="3.5"/></g></svg>
    <svg style="position:absolute;left:205px;top:57px" width="9" height="9" viewBox="0 0 9 9"><path d="M9 0L4 5l1 1 4-6zM3.5 5.5C2 5.5 1.5 7 0 8.5c2 .5 4 0 4.5-2z" fill="#3d4a66"/></svg>
    <div class="material-list" style="left:40px;top:94px;width:47px;height:23px;font-size:2.6px;padding:1px 2px"><span>Light Fixtures</span><br><span>Under Cabinet Lighting</span><br><span>Outlets</span></div>
    <div class="material-list" style="left:93px;top:94px;width:47px;height:23px;font-size:2.6px;padding:1px 2px"><span>Sink</span><br><span>Faucet</span><br><span>Sink Disposal</span></div>
    <div class="material-list" style="left:145px;top:94px;width:47px;height:23px;font-size:2.6px;padding:1px 2px"><span>Backsplash</span><br><span>Kitchen Flooring</span></div>
    <div class="material-list" style="left:198px;top:94px;width:47px;height:23px;font-size:2.6px;padding:1px 2px"><span>Trim</span><br><span>Paint Colors</span><br><span>Cabinetry &amp; Counter Tops</span></div>
  </section>

  <section class="section" style="height:163px">
    <div class="price-icon" style="width:10px;height:10px;font-size:5px;margin-top:6px">$</div>
    <h2 class="section-title" style="margin-top:5px;font-size:5.6px;letter-spacing:.2px">Pricing Packages</h2>
    <p class="center" style="margin-top:6px;font-size:3.3px;color:var(--muted)">Pricing for kitchen remodels can vary dramatically. Below you will find typical services with the varying cost levels.</p>
    <div class="price-card" style="left:40px;top:49px;width:69px;height:111px;padding-top:9px">
      <div class="price-name" style="font-size:4.5px">Minor Upgrades</div>
      <p style="font-size:2.6px;color:var(--muted);margin:3px 14px 0;line-height:1.4">Perfect for changing out some fixtures.</p>
      <div class="price-amount" style="font-size:8px;margin:4px 0 5px">$</div>
      <div class="price-list" style="font-size:2.6px;margin-left:11px;border-top:1px solid #c5ccd8;margin-right:11px;padding-top:3px"><span>Sink &amp; Fixtures</span><br><span>Backsplash</span><br><span>Cabinet Hardware</span><br><span>Paint</span><br><span>Flooring</span><br><span>Cabinetry</span><br><span>Countertops</span><br><span>Re-Route Plumbing / Electrical</span><br><span>Move Walls</span></div>
    </div>
    <div class="price-card price-card--best" style="left:108px;top:47px;width:69px;height:113px;padding-top:11px">
      <div class="badge" style="left:26px;top:1px;font-size:2px;padding:1px 3px">Best Value</div>
      <div class="price-name" style="font-size:4.5px">Moderate Remodel</div>
      <p style="font-size:2.6px;color:var(--muted);margin:3px 12px 0;line-height:1.4">Complete kitchen remodel with layout remaining the same.</p>
      <div class="price-amount" style="font-size:8px;margin:4px 0 5px">$$</div>
      <div class="price-list" style="font-size:2.6px;margin-left:11px;border-top:1px solid #e1e4ea;margin-right:11px;padding-top:3px"><span>Sink &amp; Fixtures</span><br><span>Backsplash</span><br><span>Cabinet Hardware</span><br><span>Paint</span><br><span>Flooring</span><br><span>Cabinetry</span><br><span>Countertops</span><br><span>Re-Route Plumbing / Electrical</span><br><span>Move Walls</span></div>
    </div>
    <div class="price-card" style="left:176px;top:49px;width:69px;height:111px;padding-top:9px">
      <div class="price-name" style="font-size:4.5px">Major Remodel</div>
      <p style="font-size:2.6px;color:var(--muted);margin:3px 12px 0;line-height:1.4">Complete kitchen remodel with new layout. This is a gut job.</p>
      <div class="price-amount" style="font-size:8px;margin:4px 0 5px">$$$</div>
      <div class="price-list" style="font-size:2.6px;margin-left:11px;border-top:1px solid #c5ccd8;margin-right:11px;padding-top:3px"><span>Sink &amp; Fixtures</span><br><span>Backsplash</span><br><span>Cabinet Hardware</span><br><span>Paint</span><br><span>Flooring</span><br><span>Cabinetry</span><br><span>Countertops</span><br><span>Re-Route Plumbing / Electrical</span><br><span>Move Walls</span></div>
    </div>
  </section>

  <div class="section cta-bar" style="height:19px;font-size:3.8px;gap:11px">
    <span>Schedule Your Free Consultation Today!</span>
    <span class="btn-red" style="width:56px;height:13px;font-size:3.8px">↓&nbsp; Schedule Below</span>
  </div>

  <section class="section scheduler" style="height:122px">
    <div class="clock-photo" role="img" aria-label="Close-up of a wall clock face"></div>
    <div class="booking" style="left:62px;top:2px;width:80px;height:115px;font-size:2.1px;padding:3px 4px">
      <div style="display:flex;justify-content:space-between;border-bottom:1px solid #e4e6eb;padding-bottom:2px;margin-bottom:5px"><b>Choose Appointment</b><span>Your Info</span><span>Confirmation</span></div>
      <p>Find a time that works best for your schedule below.</p>
      <p style="margin-top:6px"><b>Estimate</b><br>Meet us at your home to review the project scope.</p>
      <p style="margin-top:6px"><b>Conference Call</b><br>A quick phone chat about your project ideas.</p>
      <p style="margin-top:6px"><b>Virtual Appointment</b><br>Join a video meeting to review plans and options.</p>
      <p style="position:absolute;bottom:8px;left:0;right:0;text-align:center;font-size:1.9px">Powered by SLOTWISE SCHEDULING</p>
    </div>
    <div class="steps" style="left:145px;top:2px;width:80px;font-size:2.1px">
      <h4 style="font-size:3.6px">1. Schedule an Appointment Today</h4>
      <p style="margin:3px 0 7px">View our calendar on the left and pick a time.</p>
      <h4 style="font-size:3.6px">2. Review our "Things to Think About Checklist"</h4>
      <p style="margin:3px 0 7px">Read the checklist to prepare for your visit.</p>
      <h4 style="font-size:3.6px">3. Appointment</h4>
      <p style="margin-top:3px">A project manager will meet you to discuss details.</p>
    </div>
  </section>

  <section class="section" style="height:88px">
    <h2 class="section-title" style="padding-top:4px;font-size:4.6px;color:#555">Helpful Articles</h2>
    <div class="article" style="left:60px;top:14px;width:52px;height:50px"><div class="article-img" style="background:linear-gradient(135deg,#e5e1da,#7b6a57)" role="img" aria-label="Kitchen shelves with dishes"></div><div class="article-meta" style="font-size:1.9px">February 13, 2020<br><br>7 Key Things to Consider Before Remodeling the Kitchen</div></div>
    <div class="article" style="left:117px;top:14px;width:52px;height:50px"><div class="article-img" style="background:linear-gradient(120deg,#c45fa3,#e69a3b,#3b7fc4)" role="img" aria-label="Colourful paint splash"></div><div class="article-meta" style="font-size:1.9px">October 29, 2019<br><br>How Hard is Painting for DIY Home Renovation?</div></div>
    <div class="article" style="left:173px;top:14px;width:52px;height:50px"><div class="article-img" style="background:linear-gradient(180deg,#a9c6e2,#b88d5d)" role="img" aria-label="House under construction"></div><div class="article-meta" style="font-size:1.9px">October 24, 2019<br><br>Home Remodeling Made Easier with Simple Tips</div></div>
    <div class="btn-blog" style="left:130px;top:68px;width:25px;height:9px;font-size:1.9px">Read our Blog</div>
  </section>

  <section class="section" style="height:55px">
    <h2 class="center" style="font-family:'Poppins',sans-serif;font-weight:600;font-size:4.3px;padding-top:0">Frequently Asked Questions</h2>
    <div style="position:absolute;left:93px;top:12px;width:98px;font-size:2.2px">
      <div class="faq-row" style="padding:3px 3px"><span>How much does a kitchen remodel cost?</span><span>+</span></div>
      <div class="faq-row" style="padding:3px 3px"><span>How long will it take?</span><span>+</span></div>
      <div class="faq-row" style="padding:3px 3px"><span>Do you pull permits?</span><span>+</span></div>
      <div class="faq-row" style="padding:3px 3px"><span>Are you licensed and insured?</span><span>+</span></div>
    </div>
  </section>

  <section class="section contact" style="height:40px;padding-top:10px;font-size:3.2px;line-height:1.55">
    <h3 style="font-size:4.6px">Other Questions?</h3>
    <p>Contact us at 515-555-0142</p><p>or</p><p>Reach out to our <b>Support Team</b></p>
  </section>

  <footer class="section footer" style="height:95px">
    <div class="brand" style="position:absolute;left:57px;top:12px;font-size:7.5px"><span class="brand-dot" style="width:8px;height:8px"></span>BRELLFORGE</div>
    <div class="social" style="position:absolute;left:68px;top:24px;gap:2px"><i style="width:7px;height:7px"></i><i style="width:7px;height:7px"></i><i style="width:7px;height:7px"></i><i style="width:7px;height:7px"></i></div>
    <div class="foot-col" style="left:141px;top:12px;font-size:2.9px"><h5>SERVICES</h5>Basement Finishing<br>Bathroom Remodeling<br>Handyman<br>Kitchen Remodeling<br>Window Replacement<br>Whole Home Remodeling</div>
    <div class="foot-col" style="left:196px;top:12px;font-size:2.9px"><h5>SERVICE AREAS</h5>Ankeny, IA<br>Clive, IA<br>Des Moines, IA<br>Johnston, IA<br>Urbandale, IA<br>Waukee, IA<br>West Des Moines, IA<br>View All</div>
    <div class="copyright" style="top:74px;padding:7px 100px 0 57px;font-size:3px"><span>Copyright ©2021 <b>Brellforge</b> All Rights Reserved</span><span>⌃ Back to top</span></div>
  </footer>
</main>

<!-- Compact layout -->
<main class="page page--compact">
  <header class="section site-header" style="height:24px;padding-left:10px">
    <div class="brand" style="font-size:8px"><span class="brand-dot" style="width:8px;height:8px"></span>BRELLFORGE</div>
    <nav class="main-nav" style="font-size:4px;gap:17px;margin-left:37px"><span>Home</span><span>Services</span><span>Gallery</span><span>Blog</span><span>About</span><span>Contact</span></nav>
    <div class="estimate" style="width:72px;font-size:4.2px">GET AN ESTIMATE<br>515-555-0142</div>
  </header>

  <section class="section hero" style="height:196px">
    <div class="hero-photo" role="img" aria-label="Chrome bath faucet against dark blue panelled wall"></div>
    <h1 class="hero-title" style="left:24px;top:58px;font-size:13px">Making homes<br><span class="hero-accent" style="font-size:14px;padding:0 4px;margin-left:-5px;margin-top:2px">that matter.</span></h1>
    <p class="hero-sub" style="left:24px;top:99px;font-size:4.3px">We provide <b>home remodeling services</b> to<br>help you build a home you love.</p>
    <div class="btn-services" style="left:25px;top:122px;width:40px;height:16px;font-size:2.6px">OUR SERVICES</div>
  </section>

  <div class="section cta-bar" style="height:23px;font-size:4px;gap:37px;padding-left:30px">
    <span>Schedule a free in home consultation via our online appointment scheduling system</span>
    <span class="btn-red" style="width:42px;height:16px;font-size:4.2px">Schedule</span>
  </div>

  <section class="section projects" style="height:192px">
    <h2 class="section-title" style="padding-top:13px;font-size:9px">Get inspired by similar projects</h2>
    <div class="project" style="left:24px;top:39px;width:152px;height:101px" role="img" aria-label="White kitchen with island and pendant lights">
      <div class="project-caption" style="font-size:4px;padding:3px 4px">Kitchen and Complete Home Remodel<br>@ in Woodland Hills, CA</div></div>
    <div class="project project--two" style="left:190px;top:39px;width:151px;height:101px" role="img" aria-label="Kitchen with wood backsplash and small dining table">
      <div class="project-caption" style="font-size:4px;padding:3px 4px">Complete Kitchen Remodel<br>@ in West Hollywood, CA</div></div>
    <div class="more" style="top:150px;font-size:3.6px"><div class="more-circle" style="width:18px;height:18px;font-size:9px">+</div><div style="margin-top:3px">Show me more</div></div>
  </section>

  <section class="section bath" style="height:123px">
    <h2 class="section-title" style="padding-top:11px;font-size:8.6px">Bathroom Remodeling Made Simple.</h2>
    <p class="bath-text" style="top:31px;width:272px;font-size:6.2px">Bathroom remodel can be complex, but when completed in an eco-friendly and sustainable manner can also drastically monthly bills and give you the satisfaction of reducing your carbon footprint in the process. A bathroom remodels range anywhere from updating your plumbing fixture, to making more efficient use of the space, to building the in-home spa of your dreams. A bathroom remodel is subjective, but homeowners are generally faced with the same universal challenges regardless of project scape.</p>
    <div class="more" style="top:91px;font-size:3.6px"><div class="more-circle" style="width:18px;height:18px;font-size:9px">+</div><div style="margin-top:3px">Show me more</div></div>
  </section>

  <section class="section" style="height:72px">
    <svg class="icon-list" width="15" height="11" viewBox="0 0 11 9" style="margin-top:10px"><g fill="#3d4a66"><rect width="2" height="1.6"/><rect x="3" width="8" height="1.6"/><rect y="2.5" width="2" height="1.6"/><rect x="3" y="2.5" width="8" height="1.6"/><rect y="5" width="2" height="1.6"/><rect x="3" y="5" width="8" height="1.6"/><rect y="7.4" width="2" height="1.6"/><rect x="3" y="7.4" width="8" height="1.6"/></g></svg>
    <h2 class="section-title" style="margin-top:7px;font-size:7px;letter-spacing:.3px">Material Selections</h2>
    <div class="price-icon" style="width:10px;height:10px;font-size:5px;margin-top:4px">$</div>
    <h2 class="section-title" style="margin-top:7px;font-size:5.6px">Pricing Packages</h2>
  </section>

  <div class="section cta-bar" style="height:19px;font-size:3.8px;gap:16px">
    <span>Schedule Your Free Consultation Today!</span>
    <span class="btn-red" style="width:67px;height:16px;font-size:3.8px">↓&nbsp; Schedule Below</span>
  </div>

  <section class="section center" style="height:23px;background:#e4e4e6;font-size:9px;padding-top:4px">Helpful Articles</section>
  <section class="section center" style="height:23px;background:#c8c9cc;font-size:9px;padding-top:4px">Frequently Asked Questions</section>

  <section class="section contact" style="height:47px;padding-top:6px;font-size:5.2px;line-height:1.45">
    <h3 style="font-size:8.6px">Other Questions?</h3>
    <p>Contact us at 515-555-0142</p><p>or</p><p>Reach out to our &nbsp;<b>Support Team</b></p>
  </section>

  <footer class="section footer" style="height:113px">
    <div class="brand" style="position:absolute;left:57px;top:22px;font-size:15px;gap:4px"><span class="brand-dot" style="width:16px;height:16px"></span>BRELLFORGE</div>
    <div class="social" style="position:absolute;left:88px;top:43px;gap:3px"><i style="width:16px;height:16px"></i><i style="width:16px;height:16px"></i><i style="width:16px;height:16px"></i><i style="width:16px;height:16px"></i></div>
    <div class="foot-col" style="left:208px;top:21px;font-size:4.2px"><h5 style="font-size:5px;margin-bottom:5px">SERVICES</h5>Basement Finishing<br>Bathroom Remodeling<br>Handyman<br>Kitchen Remodeling<br>Window Replacement<br>Whole Home Remodeling</div>
    <div class="foot-col" style="left:269px;top:21px;font-size:4.2px"><h5 style="font-size:5px;margin-bottom:7px">SERVICE AREAS</h5>Ankeny, IA<br>Clive, IA<br>Des Moines, IA<br>Johnston, IA<br>Urbandale, IA<br>Waukee, IA<br>West Des Moines, IA<br>View All</div>
    <div class="copyright" style="top:97px;padding:6px 75px 0 78px;font-size:3px"><span>Copyright ©2021 <b>Brellforge</b> All Rights Reserved</span><span>⌃ Back to top</span></div>
  </footer>
</main>

</body>
</html>
```